Business card design needed

We need a new business card design for a new company based in Melbourne Australia called Tallo Ventures.
We develop new products and are about to launch our first product into the health and hygiene market.
We would like our business card to be targeted at corporate/business.
We would like to see designs that use the colours blue and white and incorporate our company name logo (attached).
We would like double sided.
We would also like an infinity symbol incorporated into the design in an unusual way (eg stretched or out of proportion).
The final design should communicate innovation.

Industry/Entity Type

Health

Contact Information for Business Card

Business Name
Name
Position
Address line 1
Address line 2
Telephone 1
Telephone 2
Email
Website

Requirements
Must have
• Company name logo (attached)
Infinity symbol incorporated into design

```html
<!DOCTYPE html>
<html lang="en">
<head>
<meta charset="utf-8">
<title>Tallo Ventures — Business Card</title>
<link rel="stylesheet" href="https://fonts.googleapis.com/css2?family=PT+Sans:wght@400;700&display=swap">
<style>
  :root {
    --page: #e9ebee;
    --card-light: #ffffff;
    --card-shade: #dfe1e4;
    --navy: #2b2f78;
    --deep-blue: #25518f;
    --sky: #1f9fd6;
    --ink: #22245a;
    --brand: #2a6fb3;
    --mist: #c9ccd1;
  }
  * { margin: 0; padding: 0; box-sizing: border-box; }
  html, body {
    width: 1200px;
    height: 900px;
    overflow: hidden;
    background: var(--page);
    font-family: "PT Sans", Arial, sans-serif;
  }
  .canvas {
    position: relative;
    width: 1200px;
    height: 900px;
  }
  .card {
    position: absolute;
    left: 250px;
    width: 700px;
    height: 400px;
    overflow: hidden;
    background: radial-gradient(ellipse at 40% 25%, var(--card-light) 0%, var(--card-shade) 100%);
    box-shadow: 0 6px 18px rgba(0, 0, 0, 0.18);
  }
  .card--front { top: 30px; }
  .card--back { top: 470px; }
  .card__swoosh {
    position: absolute;
    inset: 0;
    width: 700px;
    height: 400px;
  }
  .wordmark {
    position: absolute;
    color: var(--brand);
    font-weight: 700;
    line-height: 1;
    white-space: nowrap;
    letter-spacing: 0.5px;
  }
  .card--front .wordmark {
    left: 150px;
    top: 120px;
    font-size: 62px;
  }
  .card--back .wordmark {
    right: 40px;
    top: 88px;
    font-size: 44px;
  }
  .infinity-motif {
    position: absolute;
    left: 70px;
    top: -40px;
    width: 330px;
    height: 140px;
    border-radius: 50%;
    background: radial-gradient(ellipse at center, rgba(190, 193, 198, 0.55) 0%, rgba(210, 212, 216, 0.25) 55%, rgba(230, 231, 233, 0) 75%);
  }
  .contact {
    position: absolute;
    left: 40px;
    top: 112px;
    list-style: none;
    color: var(--ink);
    font-size: 19px;
    line-height: 1.25;
  }
  .person {
    position: absolute;
    right: 60px;
    top: 148px;
    text-align: center;
    color: var(--ink);
  }
  .person__name {
    font-size: 30px;
    line-height: 1.1;
  }
  .person__position {
    font-size: 20px;
    line-height: 1.1;
  }
</style>
</head>
<body>
<main class="canvas">

  <section class="card card--front" aria-label="Card front">
    <svg class="card__swoosh" viewBox="0 0 700 400" aria-hidden="true">
      <defs>
        <linearGradient id="frontBand" x1="0" y1="0" x2="1" y2="0">
          <stop offset="0" stop-color="#1f9fd6"/>
          <stop offset="0.5" stop-color="#25518f"/>
          <stop offset="1" stop-color="#2b2f78"/>
        </linearGradient>
      </defs>
      <path d="M0,268 Q330,300 700,215" fill="none" stroke="#2b2f78" stroke-width="9"/>
      <path d="M0,285 Q330,315 700,225 L700,400 L0,400 Z" fill="#1f9fd6"/>
      <path d="M0,325 Q380,340 700,232 L700,400 L0,400 Z" fill="url(#frontBand)"/>
    </svg>
    <div class="wordmark">Tallo Ventures</div>
  </section>

  <section class="card card--back" aria-label="Card back">
    <div class="infinity-motif" role="img" aria-label="Faint stretched infinity symbol decoration"></div>
    <svg class="card__swoosh" viewBox="0 0 700 400" aria-hidden="true">
      <defs>
        <linearGradient id="backBand" x1="0" y1="0" x2="1" y2="0">
          <stop offset="0" stop-color="#1f9fd6"/>
          <stop offset="0.5" stop-color="#25518f"/>
          <stop offset="1" stop-color="#2b2f78"/>
        </linearGradient>
      </defs>
      <path d="M0,268 Q330,300 700,215" fill="none" stroke="#2b2f78" stroke-width="9"/>
      <path d="M0,285 Q330,315 700,225 L700,400 L0,400 Z" fill="#1f9fd6"/>
      <path d="M0,325 Q380,340 700,232 L700,400 L0,400 Z" fill="url(#backBand)"/>
    </svg>
    <ul class="contact">
      <li>Address: your address here</li>
      <li>Email: email@sample.com</li>
      <li>Contact: your contact info here</li>
      <li>Website: your website here</li>
    </ul>
    <div class="wordmark">Tallo Ventures</div>
    <div class="person">
      <p class="person__name">Your name here</p>
      <p class="person__position">position</p>
    </div>
  </section>

</main>
</body>
</html>
```